Tolvane Clinica Business Card Design and print

I have attached the design I require including JPEG for company logo. I would like a copy of the art work for future needs.

Double sided - the item will not change from single

250 cards with both names on Ruth Pellow and Carol Dunmore

250 cards with Ruth Pellow only

Industry/Entity Type

Business

Contact Information for Business Card

See attached layout

```html
<!DOCTYPE html>
<html lang="en">
<head>
<meta charset="utf-8">
<title>Tolvane Clinica – Business Card</title>
<link rel="stylesheet" href="https://fonts.googleapis.com/css2?family=Quicksand:wght@300;400;500&family=Exo+2:wght@500;600&display=swap">
<style>
  :root {
    --bg: #e9e7e4;
    --card: #ffffff;
    --orange: #e8800c;
    --purple: #9b1fe0;
    --ink: #3a3a3a;
    --ink-soft: #555555;
  }
  * { box-sizing: border-box; margin: 0; padding: 0; }
  html, body { width: 1200px; height: 903px; overflow: hidden; }
  body {
    background: var(--bg);
    font-family: "Quicksand", sans-serif;
    display: flex;
    flex-direction: column;
    align-items: center;
    justify-content: center;
    gap: 36px;
  }
  .card {
    position: relative;
    width: 700px;
    height: 400px;
    background: var(--card);
    box-shadow: 0 6px 18px rgba(0,0,0,0.12);
    overflow: hidden;
  }

  /* Front */
  .front-brand {
    position: absolute;
    inset: 0;
    display: flex;
    align-items: center;
    justify-content: center;
    gap: 10px;
    color: var(--orange);
    font-weight: 300;
    font-size: 54px;
    letter-spacing: 1px;
  }
  .front-brand .word-top { align-self: center; transform: translateY(-36px); }
  .front-brand .word-bottom { align-self: center; transform: translateY(36px); }
  .brand-square {
    width: 96px;
    height: 96px;
    background: var(--purple);
  }

  /* Back */
  .corner-tab {
    position: absolute;
    left: 62px; top: 0;
    width: 62px; height: 30px;
    background: var(--purple);
  }
  .back-square {
    position: absolute;
    left: 168px; top: 38px;
    width: 92px; height: 92px;
    background: var(--purple);
  }
  .back-name {
    position: absolute;
    left: 58px; top: 118px;
    color: var(--orange);
    font-weight: 300;
    font-size: 46px;
    line-height: 44px;
    letter-spacing: 1px;
  }
  .address {
    position: absolute;
    left: 40px; top: 248px;
    display: flex;
    gap: 8px;
    color: var(--ink);
    font-size: 13px;
    line-height: 17px;
    font-weight: 500;
  }
  .address svg { flex: none; margin-top: 1px; }
  .accent-band {
    position: absolute;
    left: 390px; right: 0; top: 168px;
    height: 30px;
    background: var(--orange);
  }
  .person {
    position: absolute;
    left: 390px; top: 210px;
  }
  .person-name {
    font-family: "Exo 2", sans-serif;
    font-weight: 600;
    font-size: 20px;
    letter-spacing: 1.5px;
    color: var(--orange);
    text-transform: uppercase;
  }
  .person-role {
    font-size: 14px;
    font-weight: 500;
    color: var(--ink-soft);
    margin-top: 2px;
  }
  .contacts {
    position: absolute;
    left: 330px; top: 272px;
    list-style: none;
    font-size: 12.5px;
    font-weight: 500;
    color: var(--ink);
  }
  .contacts li {
    display: flex;
    align-items: center;
    gap: 8px;
    height: 21px;
  }
  .contacts svg { width: 12px; height: 12px; flex: none; }
</style>
</head>
<body>

  <section class="card card-front" aria-label="Business card front">
    <div class="front-brand">
      <span class="word-top">tolvane</span>
      <span class="brand-square" aria-hidden="true"></span>
      <span class="word-bottom">clinica</span>
    </div>
  </section>

  <section class="card card-back" aria-label="Business card back">
    <div class="corner-tab"></div>
    <div class="back-square" aria-hidden="true"></div>
    <div class="back-name">tolvane<br>clinica</div>

    <div class="address">
      <svg width="14" height="18" viewBox="0 0 14 18" aria-hidden="true">
        <path d="M7 0C3.1 0 0 3 0 6.8 0 11.6 7 18 7 18s7-6.4 7-11.2C14 3 10.9 0 7 0z" fill="var(--purple)"/>
        <circle cx="7" cy="6.8" r="2.6" fill="#fff"/>
      </svg>
      <p>214 6th floor, Plaza<br>Harbour Road NKT</p>
    </div>

    <div class="accent-band"></div>

    <div class="person">
      <p class="person-name">Owen Trelawny</p>
      <p class="person-role">Managing Director</p>
    </div>

    <ul class="contacts">
      <li>
        <svg viewBox="0 0 12 12" aria-hidden="true"><path d="M2.5 0.8l2 2.2-1 1.3c.6 1.4 1.8 2.6 3.2 3.2l1.3-1 2.2 2-1.2 2C5 10.6 1.4 7 .6 2z" fill="var(--orange)"/></svg>
        040 555 0193
      </li>
      <li>
        <svg viewBox="0 0 12 12" aria-hidden="true"><rect x="3" y="0.5" width="6" height="11" rx="1" fill="none" stroke="var(--orange)" stroke-width="1.3"/><circle cx="6" cy="9.6" r=".7" fill="var(--orange)"/></svg>
        040 555 0194
      </li>
      <li>
        <svg viewBox="0 0 12 12" aria-hidden="true"><rect x="1" y="4" width="10" height="6" rx="1" fill="var(--orange)"/><rect x="3" y="1" width="6" height="3" fill="var(--orange)"/></svg>
        hello@tolvane.com
      </li>
      <li>
        <svg viewBox="0 0 12 12" aria-hidden="true"><rect x="0.5" y="2" width="11" height="8" rx="1" fill="var(--orange)"/><path d="M1 2.6l5 3.8 5-3.8" fill="none" stroke="#fff" stroke-width="1"/></svg>
        www.tolvaneclinica.com
      </li>
    </ul>
  </section>

</body>
</html>
```